Need Letterhead and Business Card

I have a logo but i need new letterhead and biz cards. We are a real estate investment firm so we need very professional but also do not want to be old fashioned. We have 3 locations; Singapore, New York and Ponte Vedra Florida. I can provide full addresses if needed. If you have adjustments to our logo you would recommend we are open to them.
I will be putting in a separate project but we also need a template for our own powerpoint slide presentations and website.

Real Estate

```html
<!DOCTYPE html>
<html lang="en">
<head>
<meta charset="utf-8">
<title>Halden – Business Card</title>
<link href="https://fonts.googleapis.com/css2?family=Source+Sans+3:wght@400;600;700&display=swap" rel="stylesheet">
<style>
  :root {
    --navy: #17477b;
    --gold: #b8922f;
    --white: #ffffff;
    --backdrop: #3a2217;
  }
  * { margin: 0; padding: 0; box-sizing: border-box; }
  html, body {
    width: 1200px; height: 1079px; overflow: hidden;
    background: var(--backdrop);
    font-family: "Source Sans 3", "Myriad Pro", sans-serif;
  }
  .card {
    position: absolute;
    width: 706px; height: 402px;
    overflow: hidden;
  }
  .card-front { left: 116px; top: 111px; background: var(--white); }
  .card-back { left: 379px; top: 566px; width: 706px; height: 403px; background: var(--navy); }

  .wordmark {
    position: absolute; left: 0; right: 0;
    text-align: center;
    font-weight: 600;
    letter-spacing: 1px;
    line-height: 1;
  }
  .card-front .wordmark { top: 52px; font-size: 92px; color: var(--navy); }
  .brand-rule {
    position: absolute; left: 208px; width: 306px; top: 160px;
    height: 3px; background: var(--navy);
  }
  .tagline {
    position: absolute; left: 0; right: 0; top: 172px;
    text-align: center; font-size: 13.5px; color: var(--gold);
    letter-spacing: 0.3px; font-weight: 400;
  }
  .holder {
    position: absolute; left: 0; right: 0; top: 210px;
    text-align: center; color: var(--navy);
  }
  .holder .name { font-size: 24px; font-weight: 700; }
  .holder .title { font-size: 19px; font-weight: 400; color: var(--gold); }

  .gold-rule {
    position: absolute; left: 0; right: 0; top: 256px;
    height: 4px; background: var(--gold);
  }
  .contact-band {
    position: absolute; left: 0; right: 0; top: 262px; bottom: 0;
    background: var(--navy); color: var(--white);
    font-size: 18.5px; line-height: 25px;
  }
  .address {
    position: absolute; right: 341px; top: 34px;
    text-align: right;
  }
  .address .line-phone { display: flex; justify-content: flex-end; align-items: center; gap: 5px; }
  .divider {
    position: absolute; left: 379px; top: 38px;
    width: 1px; height: 72px; background: rgba(255,255,255,0.35);
  }
  .channels {
    position: absolute; left: 394px; top: 33px;
    list-style: none;
  }
  .channels li { display: flex; align-items: center; gap: 10px; height: 25px; }
  .channels svg { width: 16px; height: 16px; flex: none; }

  .card-back .wordmark { top: 162px; font-size: 62px; color: var(--gold); }
  .card-back .web {
    position: absolute; left: 0; right: 0; top: 230px;
    text-align: center; color: var(--white);
    font-size: 22px; letter-spacing: 6px; font-weight: 400;
  }
</style>
</head>
<body>

<section class="card card-front">
  <div class="wordmark">Halden</div>
  <div class="brand-rule"></div>
  <div class="tagline">REAL ESTATE INVESTMENT &amp; MANAGEMENT</div>
  <div class="holder"><span class="name">Your Name</span><span class="title">, Title</span></div>
  <div class="gold-rule"></div>

  <div class="contact-band">
    <div class="address">
      <div class="line-phone">
        <svg width="15" height="15" viewBox="0 0 16 16" aria-hidden="true"><circle cx="8" cy="8" r="7" fill="none" stroke="#b8922f" stroke-width="1.2"/><path d="M5.5 4.5c-.8 2.8.8 6 4 7l1-1.4-1.6-1-1 .7c-.9-.6-1.5-1.6-1.7-2.7l1.1-.5-.4-1.9z" fill="#b8922f"/></svg>
        <span>123-456-7890</span>
      </div>
      <div>Street Name, City Name,</div>
      <div>Zip Code - 00000</div>
    </div>
    <div class="divider"></div>
    <ul class="channels">
      <li>
        <svg viewBox="0 0 16 16" aria-hidden="true"><rect x="4" y="1" width="8" height="14" rx="1.5" fill="none" stroke="#b8922f" stroke-width="1.4"/><rect x="5.5" y="3" width="5" height="4" fill="#b8922f"/><circle cx="8" cy="12" r="1" fill="#b8922f"/></svg>
        <span>123-456-7890</span>
      </li>
      <li>
        <svg viewBox="0 0 16 16" aria-hidden="true"><rect x="1" y="4" width="14" height="9" fill="#b8922f"/><path d="M1 4l7 5 7-5" fill="none" stroke="#17477b" stroke-width="1.2"/></svg>
        <span>info@halden.com</span>
      </li>
      <li>
        <svg viewBox="0 0 16 16" aria-hidden="true"><g fill="none" stroke="#7f97b5" stroke-width="1"><circle cx="8" cy="8" r="6.5"/><ellipse cx="8" cy="8" rx="3" ry="6.5"/><path d="M1.5 8h13M2.5 4.8h11M2.5 11.2h11"/></g></svg>
        <span>www.halden.com</span>
      </li>
    </ul>
  </div>
</section>

<section class="card card-back">
  <div class="wordmark">Halden</div>
  <div class="web">www.halden.com</div>
</section>

</body>
</html>
```